Business Card Design

This is a card for a dental orthodontics(braces) clinic.we provide patients life changing experience by changing their smiles. Our clinic features state of the art technology . Our preferred color scheme is blue,green and purple.
Our target market is teens and adults

I have attached a logo, it can be modified in my chosen colors
Updates

Lpleaas keep in mind dr. Fennimore is almost a fresh graduate and young, so the card should b fresh and vibrant

Reason: I have not received anything very satisfactory yet

• Dear all  the logo doesn't have to b something teeth related , it can b something based on simple lines like saome boxes etc

Industry/Entity Type

Dental

Contact Information for Business Card

BROCKWELL.FENNIMORE.
ORTHODONTICS

Olwen Fennimore, DDS, MS, MSD
Smile maker

Locations:
4815 W.Partridge Lane #312, Carrollton, TX 75009

6187 Meadow Brook Drive #408, Plano, TX 75098

812 Brindlemoor, Seagoville, TX 75159

Phone:972-555-0148

```html
<!DOCTYPE html>
<html lang="en">
<head>
<meta charset="utf-8">
<title>Brockwell Fennimore Orthodontics – Business Card</title>
<link href="https://fonts.googleapis.com/css2?family=Arimo:wght@400;700&family=Great+Vibes&family=Jura:wght@400&display=swap" rel="stylesheet">
<style>
  :root {
    --bg: #e9e6e1;
    --card-light: #fbfbfb;
    --card-mid: #eceded;
    --card-edge: #dcdddd;
    --navy: #2f55a4;
    --tooth-blue: #4a6aa8;
    --tooth-deep: #38558f;
    --green: #3fc07a;
    --teal-green: #34b287;
    --shadow: rgba(40, 30, 20, 0.22);
  }
  * { margin: 0; padding: 0; box-sizing: border-box; }
  html, body { width: 1200px; height: 723px; overflow: hidden; }
  body {
    background: var(--bg);
    position: relative;
    font-family: "Arimo", Arial, sans-serif;
  }
  .card {
    position: absolute;
    top: 62px;
    width: 344px;
    height: 600px;
    overflow: hidden;
    background: linear-gradient(160deg, var(--card-light) 0%, var(--card-mid) 60%, var(--card-edge) 100%);
    box-shadow: 0 8px 24px var(--shadow);
  }
  .card--back { left: 214px; }
  .card--front { left: 642px; }

  /* Contact side */
  .doctor-name {
    position: absolute; left: 30px; top: 34px;
    font-weight: 700; font-size: 33px; color: var(--navy);
    letter-spacing: 0.2px;
    white-space: nowrap;
  }
  .doctor-degrees {
    position: absolute; left: 92px; top: 74px;
    font-weight: 700; font-size: 21px; color: var(--green);
  }
  .tagline {
    position: absolute; left: 28px; top: 122px;
    font-family: "Great Vibes", cursive;
    font-size: 50px; color: var(--green);
    white-space: nowrap;
  }
  .locations {
    position: absolute; right: 30px; top: 232px;
    text-align: right;
  }
  .locations-label {
    font-size: 13px; color: var(--green); margin-bottom: 4px;
  }
  .address {
    font-weight: 700; font-size: 14.5px; line-height: 19px;
    color: var(--navy); margin-bottom: 14px;
    white-space: nowrap;
  }
  .contact {
    position: absolute; left: 30px; top: 480px;
    font-size: 14.5px; line-height: 24px;
  }
  .contact-label { color: var(--green); font-weight: 400; margin-right: 4px; }
  .contact-value { color: var(--navy); font-weight: 700; }

  /* Logo side */
  .mark {
    position: absolute; left: 62px; top: 46px;
    width: 220px; height: 250px;
  }
  .practice-name {
    position: absolute; left: 0; right: 0; top: 356px;
    text-align: center;
    font-family: "Jura", sans-serif;
    font-size: 30px; line-height: 46px;
    letter-spacing: 4px;
    padding-left: 4px;
    color: var(--teal-green);
    white-space: nowrap;
  }
</style>
</head>
<body>

  <section class="card card--back" aria-label="Business card, contact side">
    <h1 class="doctor-name">Olwen Fennimore</h1>
    <p class="doctor-degrees">DDS,MS,MSD</p>
    <p class="tagline">Smile maker</p>
    <div class="locations">
      <p class="locations-label">locations</p>
      <p class="address">4815 W.Partridge Lane #312<br>Carrollton, TX 75009</p>
      <p class="address">6187 Meadow Brook Drive #408<br>Plano, TX 75098</p>
      <p class="address">812 Brindlemoor<br>Seagoville, TX 75159</p>
    </div>
    <div class="contact">
      <p><span class="contact-label">phone</span><span class="contact-value">972-555-0148</span></p>
      <p><span class="contact-label">fax</span><span class="contact-value">972-555-0199</span></p>
    </div>
  </section>

  <section class="card card--front" aria-label="Business card, logo side">
    <svg class="mark" viewBox="0 0 220 250" role="img" aria-label="Practice emblem with blue patterned fill">
      <defs>
        <linearGradient id="emblemFill" x1="0" y1="0" x2="1" y2="1">
          <stop offset="0" stop-color="#4a6aa8"/>
          <stop offset="1" stop-color="#38558f"/>
        </linearGradient>
      </defs>
      <rect x="0" y="0" width="220" height="250" rx="36" fill="url(#emblemFill)"/>
    </svg>
    <p class="practice-name">BROCKWELL<br>FENNIMORE<br>ORTHODONTICS</p>
  </section>

</body>
</html>
```